Every Drawer Neatly Sorted or EDN Organized needs a business card design. EDN Organized is a professi

We need a business card design that is clean, sharp and conveys a sense of organization. I already have a logo.

Target Market(s)

Families (specifically mothers), small business owners, parents, seniors

Industry/Entity Type

Business

Contact Information for Business Card

My website is www.ednorganized-example.com and my Facebook page is http://www.socialpage-example.com/everydrawerneatlysorted. The phone number is 555-418-2706 and I want to be listed as Miriel O. Dunsford, Owner

Requirements
Must have
• My logo.

```html
<!DOCTYPE html>
<html lang="en">
<head>
<meta charset="utf-8">
<title>EDN Organized – Business Card</title>
<link rel="stylesheet" href="https://fonts.googleapis.com/css2?family=Montserrat:wght@500&family=Open+Sans:wght@400&display=swap">
<style>
  :root {
    --page-bg: #2e2e2e;
    --card-white: #ffffff;
    --card-shade: #e6e7e8;
    --brand-blue: #3478bd;
    --ink: #2a2a2a;
    --ink-soft: #3c3c3c;
  }
  * { margin: 0; padding: 0; box-sizing: border-box; }
  html, body {
    width: 1200px;
    height: 848px;
    overflow: hidden;
    background: var(--page-bg);
  }
  .canvas {
    position: relative;
    width: 1200px;
    height: 848px;
  }
  .card {
    position: absolute;
    left: 120px;
    top: 148px;
    width: 960px;
    height: 552px;
    background: radial-gradient(ellipse 55% 60% at 45% 40%, var(--card-white) 0%, #f7f7f8 45%, var(--card-shade) 100%);
    overflow: hidden;
  }
  .brand {
    position: absolute;
    left: 68px;
    top: 100px;
    display: flex;
    align-items: center;
    gap: 16px;
    font-family: "Montserrat", sans-serif;
    font-weight: 500;
    font-size: 44px;
    letter-spacing: 3px;
    color: var(--ink);
  }
  .brand-mark {
    width: 18px;
    height: 18px;
    border-radius: 50%;
    background: var(--brand-blue);
  }
  .accent-bar {
    position: absolute;
    left: 0;
    top: 334px;
    width: 11px;
    height: 218px;
    background: var(--brand-blue);
  }
  .contact {
    position: absolute;
    left: 68px;
    top: 334px;
    font-family: "Open Sans", sans-serif;
    font-weight: 400;
  }
  .person-name {
    font-size: 23px;
    color: var(--brand-blue);
    text-transform: uppercase;
    line-height: 30px;
  }
  .person-role {
    font-size: 19px;
    color: var(--ink);
    line-height: 24px;
  }
  .contact-list {
    list-style: none;
    margin-top: 24px;
  }
  .contact-item {
    display: flex;
    align-items: center;
    gap: 10px;
    font-size: 20px;
    line-height: 32px;
    color: var(--ink-soft);
  }
  .contact-icon {
    width: 16px;
    height: 16px;
    flex: none;
  }
  .social-square {
    width: 13px;
    height: 13px;
    margin: 0 1px 0 2px;
    background: var(--ink-soft);
    flex: none;
  }
</style>
</head>
<body>
<main class="canvas">
  <section class="card">
    <div class="brand">
      <span class="brand-mark"></span>
      <span class="brand-name">EDN Organized</span>
    </div>

    <div class="accent-bar"></div>

    <div class="contact">
      <p class="person-name">Miriel O. Dunsford</p>
      <p class="person-role">Owner</p>
      <ul class="contact-list">
        <li class="contact-item">
          <svg class="contact-icon" viewBox="0 0 16 16" aria-hidden="true">
            <path d="M4 1.5 L6.2 4.5 L4.8 6 C5.6 8 7.6 10.2 10 11.2 L11.5 9.8 L14.5 12 L12.8 14.3 C7.5 13.8 2.2 8.5 1.7 3.2 Z" fill="#3c3c3c"/>
          </svg>
          <span>555-418-2706</span>
        </li>
        <li class="contact-item">
          <span class="social-square"></span>
          <span>everydrawerneatlysorted</span>
        </li>
        <li class="contact-item">
          <svg class="contact-icon" viewBox="0 0 16 16" aria-hidden="true">
            <circle cx="8" cy="8" r="7" fill="#3478bd"/>
            <ellipse cx="8" cy="8" rx="3" ry="7" fill="none" stroke="#fff" stroke-width="1"/>
            <line x1="1" y1="8" x2="15" y2="8" stroke="#fff" stroke-width="1"/>
          </svg>
          <span>www.ednorganized-example.com</span>
        </li>
      </ul>
    </div>
  </section>
</main>
</body>
</html>
```